I need a wordpress website for myconsulting company specialized in data privacy

I'm looking for a wordpress website for my consulting company specialized in data privacy (GDPR) and computer science.
The website will serve as entry point to for potential clients.
The website should have the following sections (I'm opened to new ideas):
- Presentation of the company
- General presentation
- Services provided with some details
- Blog/articles with tags (if possible)
- Contact
On every page of the website there should be some references to pages (such as privacy policy, legal information...)
If possible he website should be multinlingual (english and french). I'll personnally take care of the translation in french.
Regarding branding;
- Name of the company: Étienne Roubaud Conseil
- Logo is attached
- For colors to be used see attached PDF for exemple

```html
<!DOCTYPE html>
<html lang="en">
<head>
<meta charset="utf-8">
<title>Étienne Roubaud Conseil — Data Privacy &amp; Computer Science</title>
<link href="https://fonts.googleapis.com/css2?family=Exo:wght@300;400;500&family=Lato:wght@400;700&display=swap" rel="stylesheet">
<style>
:root{
  --teal:#0c93a5;
  --teal-dark:#08707f;
  --navy:#063552;
  --navy-deep:#052a42;
  --hero:#1c0b0f;
  --ink:#1d2430;
  --muted:#6b7480;
  --light:#eef3f7;
  --footer:#121418;
  --white:#ffffff;
}
*{margin:0;padding:0;box-sizing:border-box}
html,body{width:1200px;height:3690px;overflow:hidden;background:var(--white)}
body{position:relative;font-family:"Lato",sans-serif;color:var(--ink)}
.abs{position:absolute}
.display{font-family:"Exo",sans-serif;font-weight:300}
.eyebrow{font-size:14px;letter-spacing:.3px;text-transform:uppercase}
.more{position:absolute;font-size:11px;font-weight:700;text-transform:uppercase;padding:3px 0 0 10px;color:var(--ink)}
.more::before{content:"";position:absolute;left:0;top:0;width:9px;height:24px;border:3px solid var(--teal);border-right:none}
.more.light{color:var(--white)}

/* hero */
.hero-bg{position:absolute;left:0;top:0;width:1200px;height:500px}
.hero-visual{position:absolute;left:673px;top:0;width:527px;height:394px;
  background:radial-gradient(circle at 56% 42%,#6fd3f0 0%,#1f6f9a 22%,#3a1e26 58%,#1c0b0f 80%)}
.brand{position:absolute;left:129px;top:14px;display:flex;align-items:center;gap:10px;color:var(--navy)}
.brand-mark{width:26px;height:26px;background:var(--teal)}
.brand-name{font-family:"Exo",sans-serif;font-weight:400;font-size:17px;line-height:1.2}
.nav{position:absolute;top:35px;font-size:12px;color:var(--white);text-transform:uppercase}
.nav.active{color:var(--teal);padding-left:12px}
.nav.active::before{content:"";position:absolute;left:0;top:-2px;width:9px;height:24px;border:3px solid var(--teal);border-right:none}
.hero-eyebrow{left:129px;top:160px;color:var(--white);font-size:19px}
.hero-title{left:127px;top:190px;color:var(--white);font-size:57px;line-height:66px}

/* section heads */
.center{left:0;width:1200px;text-align:center}

/* presentation cards */
.card{position:absolute;top:652px;width:298px;height:326px;border:3px solid #fff;border-radius:14px;
  box-shadow:0 0 0 1px #d5dbe1,0 6px 14px rgba(0,0,0,.18);color:var(--white);text-align:center;
  background:linear-gradient(180deg,#0a5172,#052b47)}
.card.teal{background:linear-gradient(180deg,#0f9cab,#087382)}
.card .icon{position:absolute;left:120px;top:45px;width:58px;height:58px;border-radius:50%;background:rgba(255,255,255,.1);
  display:flex;align-items:center;justify-content:center}
.card h3{position:absolute;top:140px;width:100%;font-size:19px}
.card p{position:absolute;top:185px;left:30px;width:232px;font-size:11.5px;line-height:18px}
.card .more{left:115px;top:264px}

/* presentation block */
.pres-band{left:0;top:1103px;width:1200px;height:305px;background:var(--light)}
.pres-media{left:130px;top:1048px;width:459px;height:291px;background:linear-gradient(135deg,#4a5560,#2c3b47 55%,#1d2a33)}

/* services */
.services-band{left:0;top:1408px;width:1200px;height:445px;background:linear-gradient(180deg,#073f5f,#063552)}
.svc{position:absolute;top:1621px;width:299px;height:381px;background:#fff;box-shadow:0 4px 16px rgba(0,0,0,.1)}
.svc .ph{height:198px}
.svc h3{position:absolute;left:33px;top:224px;font-family:"Exo",sans-serif;font-weight:500;font-size:19px;letter-spacing:.5px}
.svc p{position:absolute;left:33px;top:258px;width:240px;font-size:11px;line-height:18px;color:var(--muted)}
.svc .more{left:36px;top:330px}

/* blog */
.post{position:absolute;top:2128px;width:299px}
.post .ph{height:200px}
.post .date{margin-top:16px;font-size:11px;color:var(--navy)}
.post h4{margin-top:5px;font-family:"Exo",sans-serif;font-weight:400;font-size:16px;color:var(--navy)}
.post p{margin-top:8px;font-size:11px;line-height:17px;color:var(--muted)}
.post .more{left:2px;top:316px}

/* contact */
.contact{left:0;top:2536px;width:1200px;height:426px;background:linear-gradient(180deg,rgba(6,53,82,.93),rgba(6,53,82,.97)),linear-gradient(90deg,#2b3a44,#4d5a62,#2b3a44)}
.field{position:absolute;background:#fff;font-size:10px;padding:13px 14px;color:var(--ink)}
.submit{position:absolute;left:610px;top:2853px;width:299px;height:36px;background:var(--teal);color:#fff;font-size:11px;font-weight:700;
  display:flex;align-items:center;justify-content:center}

/* testimonials */
.t-thumb{position:absolute;top:3030px;width:139px;height:249px;display:flex;align-items:center;justify-content:center}
.t-main{left:291px;top:3030px;width:219px;height:249px;background:linear-gradient(180deg,#d7cbbf,#8e7d70)}

/* footer */
.foot-bg{position:absolute;left:0;top:3340px;width:1200px;height:350px}
.foot-h{position:absolute;top:3456px;font-family:"Exo",sans-serif;font-weight:300;font-size:19px;color:#fff}
.foot-list{position:absolute;top:3495px;list-style:none;font-size:11px;color:#d9dde2;line-height:28.2px}
.social{position:absolute;top:3544px;width:20px;height:20px;border:1px solid #fff}
</style>
</head>
<body>

<!-- HERO -->
<svg class="hero-bg" viewBox="0 0 1200 500" aria-hidden="true">
  <polygon points="0,90 380,90 472,0 1200,0 1200,394 740,394 660,467 0,467" fill="#1c0b0f"/>
  <polygon points="0,480 652,480 745,394 1200,394 1200,415 754,415 662,492 0,492" fill="#0c93a5"/>
</svg>
<div class="hero-visual" role="img" aria-label="Hands sheltering a glowing digital padlock shield"></div>
<svg class="abs" style="left:0;top:0" width="1200" height="100" aria-hidden="true">
  <polygon points="0,0 472,0 380,90 0,90" fill="#fff"/>
</svg>
<div class="brand"><span class="brand-mark"></span><span class="brand-name">Étienne Roubaud<br>Conseil</span></div>
<span class="nav active" style="left:608px">Home</span>
<span class="nav" style="left:707px">About</span>
<span class="nav" style="left:802px">Services</span>
<span class="nav" style="left:911px">Blog</span>
<span class="nav" style="left:995px">Contact Us</span>
<p class="abs hero-eyebrow">SPECIALIZED IN</p>
<h1 class="abs display hero-title">Data Privacy &amp;<br>Computer Science</h1>
<span class="more light" style="left:129px;top:358px;font-size:14px;font-weight:400;padding-left:15px">Get Started</span>

<!-- GENERAL PRESENTATION -->
<p class="abs center eyebrow" style="top:562px;font-size:14px">Étienne Roubaud Conseil</p>
<h2 class="abs center display" style="top:580px;font-size:34px;font-weight:400">General Presentation</h2>

<div class="card" style="left:130px">
  <div class="icon"><svg width="34" height="34" viewBox="0 0 34 34" fill="none" stroke="#fff" stroke-width="1.6"><path d="M17 3 L28 7 V16 C28 23 23 28 17 31 C11 28 6 23 6 16 V7 Z"/><circle cx="17" cy="15" r="4"/><path d="M11 24 C12 20 22 20 23 24"/></svg></div>
  <h3 class="display">Denouncing Pleasure</h3>
  <p>Sed ut perspiciatis unde omnis iste natus error sit voluptatem accusantium doloremque laudantium</p>
  <span class="more light">Read More</span>
</div>
<div class="card teal" style="left:451px">
  <div class="icon"><svg width="34" height="34" viewBox="0 0 34 34" fill="none" stroke="#fff" stroke-width="1.6"><rect x="5" y="7" width="24" height="16"/><path d="M3 27 H31"/><rect x="14" y="13" width="6" height="5"/><path d="M15 13 V11 A2 2 0 0 1 19 11 V13"/></svg></div>
  <h3 class="display">Finibus Bonorum</h3>
  <p>Sed ut perspiciatis unde omnis iste natus error sit voluptatem accusantium doloremque laudantium</p>
  <span class="more light">Read More</span>
</div>
<div class="card" style="left:772px">
  <div class="icon"><svg width="34" height="34" viewBox="0 0 34 34" fill="none" stroke="#fff" stroke-width="1.6"><rect x="8" y="12" width="18" height="13"/><path d="M5 29 H29"/><circle cx="10" cy="6" r="2.5"/><circle cx="17" cy="6" r="2.5"/><circle cx="24" cy="6" r="2.5"/><circle cx="17" cy="17" r="2.5"/></svg></div>
  <h3 class="display">Human Happiness</h3>
  <p>Sed ut perspiciatis unde omnis iste natus error sit voluptatem accusantium doloremque laudantium</p>
  <span class="more light">Read More</span>
</div>

<!-- COMPANY PRESENTATION -->
<div class="abs pres-band"></div>
<div class="abs pres-media" role="img" aria-label="Consultant presenting a data analysis chart to a meeting">
  <svg class="abs" style="left:199px;top:115px" width="60" height="60" viewBox="0 0 60 60" aria-hidden="true"><circle cx="30" cy="30" r="26" fill="none" stroke="#fff" stroke-width="2.5"/><polygon points="24,19 41,30 24,41" fill="#fff"/></svg>
</div>
<p class="abs eyebrow" style="left:610px;top:1144px">Presentation</p>
<h2 class="abs display" style="left:609px;top:1162px;font-size:33px;font-weight:400">Étienne Roubaud Conseil</h2>
<p class="abs" style="left:610px;top:1216px;width:460px;font-size:12px;line-height:18px;color:var(--muted)">Sed ut perspiciatis unde omnis iste natus error sit voluptatem accusantium doloremque laudantium, totam rem aperiam, eaque ipsa quae ab illo inventore veritatis et quasi architecto beatae vitae dicta sunt explicabo. Nemo enim ipsam voluptatem quia voluptas sit aspernatur...</p>
<span class="more" style="left:611px;top:1311px">Read More</span>

<!-- SERVICES -->
<div class="abs services-band"></div>
<p class="abs center eyebrow" style="top:1454px;color:#fff">Services</p>
<h2 class="abs center display" style="top:1473px;font-size:33px;color:#fff">What We Offer</h2>
<p class="abs" style="left:210px;top:1533px;width:780px;text-align:center;font-size:12.5px;line-height:21px;color:#e3ebf1">Sed ut perspiciatis unde omnis iste natus error sit voluptatem accusantium doloremque laudantium, totam rem aperiam, eaque ipsa quae ab illo inventore veritatis et quasi architecto beatae vitae dicta sunt explicabo.</p>

<div class="svc" style="left:130px">
  <div class="ph" role="img" aria-label="Tablet showing data protection on a wooden desk" style="background:linear-gradient(135deg,#6b4a33,#3c2a1f)"></div>
  <h3>Expedita Distinctio</h3>
  <p>But I must explain to you how all this mistaken idea of denouncing pleasure and praising pain was born...</p>
  <span class="more">Read More</span>
</div>
<div class="svc" style="left:451px">
  <div class="ph" role="img" aria-label="Laptop keyboard with a holographic security padlock" style="background:linear-gradient(135deg,#0c2a4a,#1a6d9a 55%,#0a1c33)"></div>
  <h3>Some Advantage</h3>
  <p>But I must explain to you how all this mistaken idea of denouncing pleasure and praising pain was born...</p>
  <span class="more">Read More</span>
</div>
<div class="svc" style="left:772px">
  <div class="ph" role="img" aria-label="Woman working on a laptop at a bright desk" style="background:linear-gradient(135deg,#e9ded3,#b89a82)"></div>
  <h3>Corporis Suscipit</h3>
  <p>But I must explain to you how all this mistaken idea of denouncing pleasure and praising pain was born...</p>
  <span class="more">Read More</span>
</div>

<!-- BLOG -->
<h2 class="abs center display" style="top:2064px;font-size:33px;font-weight:400">Recent Blog</h2>
<div class="post" style="left:130px">
  <div class="ph" role="img" aria-label="Team working at computer monitors with code" style="background:linear-gradient(135deg,#3a3f3c,#5a5c52 50%,#262a2a)"></div>
  <p class="date">16th Jan, 2022</p>
  <h4>Nemo enim ipsam voluptatem quia</h4>
  <p>Nor again is there anyone who loves or pursues or desires to obtain pain...</p>
  <span class="more">Read More</span>
</div>
<div class="post" style="left:451px">
  <div class="ph" role="img" aria-label="Finger touching a gear with security icons around it" style="background:linear-gradient(135deg,#9aa79d,#c1c9bf)"></div>
  <p class="date">16th Jan, 2022</p>
  <h4>Nemo enim ipsam voluptatem quia</h4>
  <p>Nor again is there anyone who loves or pursues or desires to obtain pain...</p>
  <span class="more">Read More</span>
</div>
<div class="post" style="left:772px">
  <div class="ph" role="img" aria-label="Hands using a tablet with data charts overlay" style="background:linear-gradient(135deg,#0e2a58,#2f5d9e 55%,#d9dde6)"></div>
  <p class="date">16th Jan, 2022</p>
  <h4>Nemo enim ipsam voluptatem quia</h4>
  <p>Nor again is there anyone who loves or pursues or desires to obtain pain...</p>
  <span class="more">Read More</span>
</div>

<!-- CONTACT -->
<div class="abs contact" role="img" aria-label="Office team working, tinted in navy"></div>
<h2 class="abs center display" style="top:2600px;font-size:33px;color:#fff">Reach Us</h2>
<p class="abs center" style="top:2645px;font-size:12.5px;color:#e3ebf1">Nemo enim ipsam voluptatem quia voluptas sit aspernatur</p>
<div class="field" style="left:289px;top:2691px;width:300px;height:36px">Firste Name:</div>
<div class="field" style="left:289px;top:2745px;width:300px;height:36px">Last Name:</div>
<div class="field" style="left:289px;top:2798px;width:300px;height:36px">Email:</div>
<div class="field" style="left:289px;top:2853px;width:300px;height:36px">Phone:</div>
<div class="field" style="left:610px;top:2691px;width:299px;height:143px">Message:</div>
<div class="submit">SUBMIT</div>

<!-- TESTIMONIALS -->
<div class="t-thumb" style="left:130px;background:linear-gradient(180deg,#4f6a86,#2e4a66)" role="img" aria-label="Previous client portrait, tinted blue">
  <svg width="30" height="10" viewBox="0 0 30 10" aria-hidden="true"><path d="M29 5 H2 M6 1 L2 5 L6 9" stroke="#fff" stroke-width="1.4" fill="none"/></svg>
</div>
<div class="abs t-main" role="img" aria-label="Portrait of a smiling client"></div>
<h2 class="abs display" style="left:529px;top:3052px;font-size:33px;font-weight:400">Testimonials</h2>
<p class="abs" style="left:530px;top:3114px;width:375px;font-size:12px;line-height:20px;color:var(--muted)">Sed ut perspiciatis unde omnis iste natus error sit voluptatem accusantium doloremque laudantium, totam rem aperiam, eaque ipsa quae ab illo inventore veritatis et quasi architecto beatae vitae dicta sunt explicabo.</p>
<p class="abs display" style="left:530px;top:3213px;font-size:17px;font-weight:400">Maren Solvik</p>
<p class="abs" style="left:530px;top:3238px;font-size:12px;color:var(--muted)">Consultant</p>
<div class="t-thumb" style="left:931px;background:linear-gradient(180deg,#4f6a86,#2e4a66)" role="img" aria-label="Next client portrait, tinted blue">
  <svg width="30" height="10" viewBox="0 0 30 10" aria-hidden="true"><path d="M1 5 H28 M24 1 L28 5 L24 9" stroke="#fff" stroke-width="1.4" fill="none"/></svg>
</div>

<!-- FOOTER -->
<svg class="foot-bg" viewBox="0 0 1200 350" aria-hidden="true">
  <polygon points="0,67 669,67 766,8 1200,8 1200,350 0,350" fill="#121418"/>
</svg>
<h3 class="foot-h" style="left:130px">Sitemap</h3>
<ul class="foot-list" style="left:130px"><li>Home</li><li>About Us</li><li>Services</li><li>Blog</li><li>Contact Us</li></ul>
<h3 class="foot-h" style="left:290px">Services</h3>
<ul class="foot-list" style="left:290px"><li>Doloremque lLaudantium</li><li>Finibus Bonorum</li><li>Pursues or Desires</li><li>Annoying Consequences</li></ul>
<h3 class="foot-h" style="left:509px">Contacts</h3>
<svg class="abs" style="left:509px;top:3497px" width="11" height="15" viewBox="0 0 11 15" aria-hidden="true"><path d="M5.5 14 C2 9 1 7 1 5 A4.5 4.5 0 0 1 10 5 C10 7 9 9 5.5 14 Z" fill="#0c93a5"/><circle cx="5.5" cy="5" r="1.6" fill="#121418"/></svg>
<p class="abs" style="left:526px;top:3494px;font-size:11px;line-height:15px;color:#d9dde2">22B/4 lorem ipsum rd, Northvale<br>Brackton, 4812Q USA</p>
<svg class="abs" style="left:509px;top:3558px" width="12" height="12" viewBox="0 0 12 12" aria-hidden="true"><path d="M2 1 L4.5 1 L5.5 4 L4 5 C5 7 6 8 8 9 L9 7.5 L12 8.5 V11 C6 11.5 0.5 6 1 1 Z" fill="#0c93a5"/></svg>
<p class="abs" style="left:526px;top:3557px;font-size:11px;color:#d9dde2">+2 (555) 240 7300</p>
<svg class="abs" style="left:509px;top:3610px" width="12" height="9" viewBox="0 0 12 9" aria-hidden="true"><rect x="0.5" y="0.5" width="11" height="8" fill="#0c93a5"/><path d="M0.5 0.5 L6 5 L11.5 0.5" stroke="#121418" fill="none"/></svg>
<p class="abs" style="left:526px;top:3606px;font-size:11px;color:#d9dde2">info@etienneroubaudconseil.com</p>

<div class="abs" style="left:769px;top:3420px;width:302px;text-align:center;color:#fff">
  <span style="display:inline-block;width:34px;height:34px;border:3px solid #fff"></span>
  <p style="margin-top:14px;font-family:'Exo',sans-serif;font-weight:400;font-size:22px;letter-spacing:1px">Étienne Roubaud Conseil</p>
</div>
<span class="social" style="left:881px"></span>
<span class="social" style="left:909px"></span>
<span class="social" style="left:939px"></span>
<p class="abs" style="left:769px;top:3587px;width:302px;text-align:center;font-size:11px;line-height:17px;color:#fff">Copyright © 2022<br><span style="color:var(--teal)">Étienne Roubaud Conseil</span>. All Rights Reserved.</p>

</body>
</html>
```